Wellspring Care Alliance Vonzo Ads

We want an ad created for the gay dating app vonzo. The size is 300x250. We want the ad to be sexy, with a shirtless man. We are advertising our free HIV and PrEP services. We are open to slogans about maybe "Bringing HIV and PrEP To You"
"Free PrEP and HIV Management"
Open to ideas.

We also offer through the Harborlight Support Fund
Copay Assistance, Insurance Premium Assistance, Free Medical Services, etc
Our website is wcanj.org

I do want the ad to have a Book Now Button

Gay sexually active males

```html
<!DOCTYPE html>
<html lang="en">
<head>
<meta charset="utf-8">
<title>Wellspring Care Alliance – Free PrEP and HIV Management</title>
<link href="https://fonts.googleapis.com/css2?family=Antonio:wght@400;600;700&family=Allura&family=Montserrat:wght@700;800&display=swap" rel="stylesheet">
<style>
  :root {
    --stage: #808080;
    --blue: #2f56e6;
    --violet: #8b3fe0;
    --pink: #f04bd3;
    --coral: #ff5a6e;
    --orange: #ff7a3d;
    --ink: #111111;
    --white: #ffffff;
    --wood-dark: #3a2a1d;
    --wood-mid: #7a5a3f;
    --wood-light: #a88a6a;
    --skin: #c48f6a;
  }
  * { margin: 0; padding: 0; box-sizing: border-box; }
  html, body {
    width: 1200px; height: 1034px; overflow: hidden;
    background: var(--stage);
  }
  .ad {
    position: absolute; left: 100px; top: 100px;
    width: 1000px; height: 832px;
    background: var(--white);
    overflow: hidden;
  }
  .ad__photo {
    position: absolute; left: 0; top: 0; width: 1000px; height: 700px;
    background:
      radial-gradient(ellipse 220px 380px at 820px 420px, var(--skin) 0%, rgba(196,143,106,0.6) 55%, rgba(196,143,106,0) 100%),
      linear-gradient(180deg, var(--wood-mid) 0%, var(--wood-dark) 35%, var(--wood-light) 60%, var(--wood-dark) 100%);
  }
  .ad__band {
    position: absolute; left: 0; top: 696px; width: 1000px; height: 12px;
    background: linear-gradient(90deg, var(--blue), var(--violet) 35%, var(--pink) 65%, var(--orange));
  }
  .ad__art { position: absolute; left: 0; top: 0; }
  .offer-intro {
    position: absolute; left: 58px; top: 396px;
    font-family: "Antonio", sans-serif; font-weight: 700;
    font-size: 38px; line-height: 43px; color: var(--white);
    white-space: nowrap;
  }
  .benefit-label {
    position: absolute; top: 620px; width: 260px; margin-left: -130px;
    text-align: center; white-space: nowrap;
    font-family: "Antonio", sans-serif; font-weight: 600;
    font-size: 30px; line-height: 29px; color: var(--white);
  }
  .book-box {
    position: absolute; left: 704px; top: 612px; width: 224px; height: 62px;
    background: var(--ink); color: var(--white);
    font-family: "Montserrat", sans-serif; font-weight: 800;
    font-size: 54px; line-height: 62px; text-align: center; letter-spacing: 2px;
  }
  .brand {
    position: absolute; left: 60px; top: 742px;
    display: flex; align-items: center; gap: 14px;
  }
  .brand__dot {
    width: 56px; height: 56px; border-radius: 50%;
    background: var(--violet);
  }
  .brand__name {
    font-family: "Montserrat", sans-serif; font-weight: 700;
    font-size: 22px; line-height: 26px; color: var(--blue);
  }
  .contact {
    position: absolute; left: 380px;
    font-family: "Montserrat", sans-serif; font-weight: 700; color: var(--ink);
  }
  .contact--web { top: 726px; font-size: 31px; }
  .contact--phone { top: 770px; font-size: 37px; }
</style>
</head>
<body>
<div class="ad">
  <div class="ad__photo" role="img" aria-label="Smiling shirtless man giving a thumbs up in front of stacked weathered plywood sheets"></div>
  <div class="ad__band"></div>

  <svg class="ad__art" width="1000" height="832" viewBox="0 0 1000 832" aria-hidden="true">
    <defs>
      <linearGradient id="headline-grad" x1="60" y1="0" x2="700" y2="0" gradientUnits="userSpaceOnUse">
        <stop offset="0" stop-color="#2f56e6"/>
        <stop offset="0.45" stop-color="#8b3fe0"/>
        <stop offset="0.7" stop-color="#f04bd3"/>
        <stop offset="1" stop-color="#ff5a6e"/>
      </linearGradient>
      <linearGradient id="circle-blue" x1="0" y1="0" x2="1" y2="1">
        <stop offset="0" stop-color="#2f56e6"/><stop offset="1" stop-color="#1f3fc4"/>
      </linearGradient>
      <linearGradient id="circle-violet" x1="0" y1="0" x2="1" y2="1">
        <stop offset="0" stop-color="#8b3fe0"/><stop offset="1" stop-color="#d94bd6"/>
      </linearGradient>
      <linearGradient id="circle-coral" x1="0" y1="0" x2="1" y2="1">
        <stop offset="0" stop-color="#f04b8a"/><stop offset="1" stop-color="#ff6a4a"/>
      </linearGradient>
      <linearGradient id="now-grad" x1="656" y1="0" x2="972" y2="0" gradientUnits="userSpaceOnUse">
        <stop offset="0" stop-color="#2f56e6"/>
        <stop offset="0.5" stop-color="#d94be0"/>
        <stop offset="1" stop-color="#ff6a4a"/>
      </linearGradient>
    </defs>

    <g class="headline" font-family="Antonio, sans-serif" font-weight="700" fill="url(#headline-grad)" stroke="#ffffff" stroke-width="3" paint-order="stroke">
      <text x="60" y="284" font-size="300" textLength="364" lengthAdjust="spacingAndGlyphs">FREE</text>
      <text x="444" y="136" font-size="130" textLength="248" lengthAdjust="spacingAndGlyphs">PREP</text>
      <text x="444" y="282" font-size="128" textLength="160" lengthAdjust="spacingAndGlyphs">HIV</text>
      <text x="60" y="376" font-size="88" textLength="480" lengthAdjust="spacingAndGlyphs">MANAGEMENT</text>
    </g>
    <text x="452" y="178" font-family="Allura, cursive" font-size="100" fill="none" stroke="#f04bd3" stroke-width="2" textLength="156" lengthAdjust="spacingAndGlyphs" transform="rotate(-12 530 160)">And</text>

    <line x1="112" y1="550" x2="508" y2="550" stroke="#c070e0" stroke-width="2"/>

    <circle cx="112" cy="550" r="66" fill="none" stroke="#2f56e6" stroke-width="1" stroke-dasharray="60 14"/>
    <circle cx="112" cy="550" r="57" fill="url(#circle-blue)"/>
    <circle cx="112" cy="550" r="46" fill="#f4f5fb"/>
    <g fill="none" stroke="#2f56e6" stroke-width="2">
      <circle cx="112" cy="536" r="9"/>
      <path d="M112 531v10M107 536h10"/>
      <circle cx="96" cy="548" r="5"/><circle cx="128" cy="548" r="5"/>
      <path d="M88 566c0-8 4-11 8-11s8 3 8 11M120 566c0-8 4-11 8-11s8 3 8 11M98 560h28v8h-28z"/>
    </g>

    <circle cx="310" cy="550" r="66" fill="none" stroke="#8b3fe0" stroke-width="1" stroke-dasharray="60 14"/>
    <circle cx="310" cy="550" r="57" fill="url(#circle-violet)"/>
    <circle cx="310" cy="550" r="46" fill="#f4f5fb"/>
    <g fill="none" stroke="#8b3fe0" stroke-width="2">
      <path d="M310 552c-14-10-18-16-18-22a9 9 0 0 1 18-2a9 9 0 0 1 18 2c0 6-4 12-18 22z"/>
      <path d="M290 538h10l4-6 5 12 4-6h16"/>
      <path d="M288 566l10-6h12c4 0 4 5 0 5h-8M310 565l14-6c4-2 6 3 2 5l-16 8h-22"/>
    </g>

    <circle cx="508" cy="550" r="66" fill="none" stroke="#ff5a6e" stroke-width="1" stroke-dasharray="60 14"/>
    <circle cx="508" cy="550" r="57" fill="url(#circle-coral)"/>
    <circle cx="508" cy="550" r="46" fill="#f4f5fb"/>
    <g fill="none" stroke="#f0504e" stroke-width="2">
      <circle cx="508" cy="528" r="8"/>
      <path d="M494 570v-30h28v30M484 570v-20h10M522 550h10v20M480 570h56M503 548h10M508 543v10M503 570v-8h10v8"/>
    </g>

    <path d="M656 660 L972 652 L960 756 L864 756 L816 802 L768 756 L672 756 Z" fill="url(#now-grad)"/>
    <text x="816" y="744" text-anchor="middle" font-family="Montserrat, sans-serif" font-weight="800" font-size="78" fill="#ffffff" letter-spacing="2">NOW!</text>

    <g transform="translate(352 746)" fill="none" stroke="#8b3fe0" stroke-width="2.2">
      <circle r="14"/>
      <ellipse rx="6" ry="14"/>
      <path d="M-14 0h28M-12-7h24M-12 7h24"/>
    </g>
    <g transform="translate(352 792)" fill="none" stroke="#2f56e6" stroke-width="3" stroke-linecap="round">
      <path d="M-12-10c-4 4-2 14 6 20s14 6 18 2l-5-6-5 2c-4-2-7-5-8-9l2-5z"/>
      <path d="M2-12a12 12 0 0 1 11 11M2-5a5 5 0 0 1 5 5" stroke="#ff5a6e"/>
    </g>
  </svg>

  <p class="offer-intro">WE ALSO OFFER THROUGH THE<br>HARBORLIGHT SUPPORT FUND</p>

  <p class="benefit-label" style="left:114px">COPAY<br>ASSISTANCE</p>
  <p class="benefit-label" style="left:310px">INSURANCE PREMIUM<br>ASSISTANCE</p>
  <p class="benefit-label" style="left:508px">FREE MEDICAL<br>SERVICES</p>

  <div class="book-box">BOOK</div>

  <div class="brand">
    <span class="brand__dot"></span>
    <span class="brand__name">Wellspring Care<br>Alliance</span>
  </div>

  <p class="contact contact--web">www.wcanj.org</p>
  <p class="contact contact--phone">201-555-0148</p>
</div>
</body>
</html>
```